Vending machine company website for SnackHarbor

We need a website for our vending machine services company. It will be based on another website that a friend has. My URL is snackharbor.com and the one I'm trying to emulate with my own logo and colors is pantrybloxo.com.

This will be roughly 6 total pages with one being an opt-in/opt-out page for SMS messages, one being a contact form, etc.

I want to use the logo I purchased from this site that I have attached.

The goal is to be clean, professional, intuitive and easy navigation, etc.

The only difference between my site and the reference site should be that we are not offering coffee service.

I will need all of the code for the site, and it should not use any CMS things like Joomla, Wordpress, etc.

Our actual machines are this model minus the green highlights.f

https://www.kelvomat.com/krx-pdl-mq-snack-and-drink-vending-machine-374.html

Target Market(s)

Companies that want to have vending machine services, or to buy or lease vending machines

Industry/Entity Type

Vending machines for snacks and drinks either placed at locations like apartment complexes, waiting rooms for tire centers, office building break rooms, etc. also vending machine repair services, or selling or leasing vending machines to those interested in getting into the business.

Coding

Coded - Design and coding required

Number of Pages Required

5+ page

Font styles to use
Sans Serif

Requirements
Must have
• It will be similar to pantrybloxo.com in terms of pages, categories, etc. but with our logo, colors, etc. and should be clean and professional. It will have the same pages plus one other page for opt-in or opt-out of SMS messages
Nice to have
• Clean graphics and perhaps some AI designs for vending machine repair, just like the one they use on the pantrybloxo.com site. We would like multiple photos on the home page cycling where you see very attractive people shopping for snacks and drinks at the machines with the items blurred, or people sitting around laughing and smiling while enjoying snacks or drinks at a campus break room, or picnic table, or outside with the machine behind them. Please search for KRX-PDL-47M(B2) Snack And Drink Vending Machine at kelvomat
Should not have
• It can not be designed for CRM like WordPress, Joomla, etc. and should be clean new code, that doesn't attract hackers and it shouldn't be too busy.

```html
<!DOCTYPE html>
<html lang="en">
<head>
<meta charset="utf-8">
<title>SnackHarbor – Landing Page Mobile View</title>
<link href="https://fonts.googleapis.com/css2?family=Montserrat:wght@500;600&family=Open+Sans:wght@400;600;700&display=swap" rel="stylesheet">
<style>
  :root{
    --bg:#f6f6f7;
    --cream:#f4f3e4;
    --cream-light:#fafaf2;
    --orange:#d9923b;
    --orange-soft:#dfa760;
    --ink:#2a2a2a;
    --muted:#6d6d6d;
    --navy:#0e4f78;
    --white:#ffffff;
    --dark:#1c1c1c;
  }
  *{box-sizing:border-box;margin:0;padding:0}
  html,body{width:1200px;height:1200px;overflow:hidden}
  body{background:var(--bg);font-family:"Open Sans",sans-serif;color:var(--ink);position:relative}

  .brand{position:absolute;left:40px;top:104px;width:270px}
  .brand-name{font-family:"Montserrat",sans-serif;font-weight:500;font-size:40px;letter-spacing:-0.5px;color:var(--orange);line-height:1;white-space:nowrap}
  .brand-sub{display:flex;align-items:center;gap:12px;margin-top:12px;padding:0 18px;font-family:"Montserrat",sans-serif;font-size:12px;letter-spacing:6px;color:var(--ink)}
  .brand-sub::before,.brand-sub::after{content:"";flex:1;height:1px;background:#888}
  .deck-label{position:absolute;left:40px;top:226px;font-size:27px;line-height:34px;color:var(--navy);font-weight:400}

  .screen{position:absolute;width:260px;border-radius:16px;overflow:hidden;background:var(--cream);box-shadow:0 12px 30px rgba(0,0,0,.08)}
  .photo{display:block}

  .btn{display:inline-flex;align-items:center;gap:8px;background:var(--orange);color:var(--white);font-size:11px;font-weight:600;border-radius:999px;padding:9px 18px}
  .btn svg{width:12px;height:12px}

  /* benefits */
  .benefits{left:40px;top:320px;height:470px;background:var(--cream)}
  .benefits .top{padding:16px 18px 20px}
  .benefits .spec-line{font-size:9px;color:var(--muted);margin-bottom:10px}
  .benefits .panel{background:var(--orange);padding:24px 18px;height:390px}
  .benefits h3{font-weight:400;font-size:21px;line-height:28px;color:var(--white)}
  .arrows{display:flex;gap:12px;margin:16px 0}
  .arrow-dot{width:26px;height:26px;border-radius:50%;display:flex;align-items:center;justify-content:center}
  .arrow-dot.off{background:#c9b9a0}
  .arrow-dot.on{background:#5a5a5a}
  .arrow-dot svg{width:11px;height:11px}
  .cards{display:flex;gap:12px}
  .benefit-card{flex:0 0 190px;background:rgba(255,255,255,.22);border-radius:10px;padding:14px;color:var(--white)}
  .benefit-card .num{font-size:20px;font-weight:700}
  .benefit-card h4{font-size:13px;font-weight:400;margin:6px 0 8px}
  .benefit-card p{font-size:10px;line-height:15px}

  /* product */
  .product{background:var(--cream);padding:16px 18px}
  .product .eyebrow{font-size:9px;color:var(--orange);font-weight:700}
  .product h3{font-size:14px;font-weight:400;line-height:19px;margin:6px 0 12px}
  .thumbs{display:flex;gap:8px;margin:12px 0}
  .thumbs span{width:34px;height:34px;border-radius:4px;border:1px solid #ccc;background:linear-gradient(#5a2020,#2a2a2a)}
  .thumbs span.active{border:2px solid var(--orange)}
  .spec dt{font-size:11px;font-weight:600;margin-top:6px}
  .spec dd{font-size:10px;color:var(--muted)}
  .product-a{left:40px;top:810px;height:350px}
  .product-b{left:620px;top:40px;height:520px}

  /* testimonials */
  .testimonials{left:330px;top:40px;height:250px;padding:16px;display:flex;gap:12px;background:var(--cream)}
  .review{flex:0 0 180px;background:var(--white);border-radius:10px;padding:14px}
  .avatar{width:54px;height:54px;border-radius:10px;background:linear-gradient(135deg,#b58a5e,#4c4a3a);margin-bottom:10px}
  .review h5{font-size:11px;font-weight:600}
  .review .age{font-size:9px;color:var(--muted);margin-bottom:8px}
  .review p{font-size:9px;line-height:14px;color:var(--muted)}

  /* inventory */
  .inventory{left:330px;top:310px;height:250px;background:var(--cream-light);padding:18px}
  .inventory h3{font-size:20px;font-weight:400;color:var(--orange);line-height:26px;margin-bottom:14px}

  /* hero */
  .hero{left:330px;top:580px;height:580px;background:var(--dark);border-radius:22px}
  .hero .bgimg{position:absolute;inset:0;background:linear-gradient(160deg,#2f3b48 0%,#3a5a6c 35%,#5a4a3a 65%,#151515 100%)}
  .hero .shade{position:absolute;inset:0;background:linear-gradient(180deg,rgba(0,0,0,.35),rgba(0,0,0,.55))}
  .hero-bar{position:relative;display:flex;justify-content:space-between;align-items:center;padding:16px 18px}
  .hero-logo{font-family:"Montserrat",sans-serif;font-size:16px;font-weight:500;color:var(--orange)}
  .burger{width:16px;height:10px;border-top:2px solid #fff;border-bottom:2px solid #fff;position:relative}
  .hero-body{position:relative;padding:120px 20px 0}
  .hero h1{color:var(--white);font-weight:400;font-size:26px;line-height:33px}
  .hero .lede{color:var(--orange);font-size:10.5px;font-weight:600;line-height:16px;margin:16px 0 22px}

  /* benefits + faq */
  .faq-screen{left:620px;top:580px;height:580px;background:var(--cream)}
  .faq-screen .panel{background:var(--orange);padding:18px;height:270px;display:flex;gap:12px}
  .faq-body{padding:18px}
  .faq-body .eyebrow{font-size:9px;color:var(--orange);font-weight:700}
  .faq-body h3{font-size:15px;font-weight:400;line-height:21px;margin:6px 0 14px}
  .faq-item{background:var(--white);border-left:3px solid var(--orange);padding:12px;margin-bottom:10px;font-size:10px}
  .faq-item h5{font-size:10px;font-weight:600;display:flex;justify-content:space-between;gap:8px}
  .faq-item p{font-size:8.5px;line-height:13px;color:var(--muted);margin-top:6px}

  /* footer */
  .footer{left:910px;top:40px;height:520px;background:var(--white);padding:22px}
  .footer-logo{font-family:"Montserrat",sans-serif;font-size:26px;font-weight:500;color:var(--orange)}
  .socials{display:flex;gap:12px;margin:14px 0 18px}
  .socials span{width:24px;height:24px;border-radius:50%;background:var(--orange)}
  .socials span.light{background:#eef0f4}
  .footer h6{font-size:11px;font-weight:700;margin-bottom:8px}
  .footer ul{list-style:none;margin-bottom:18px}
  .footer li{font-size:11px;margin-bottom:7px}
  .contact li{display:flex;gap:8px;align-items:flex-start;line-height:15px}
  .contact svg{width:12px;height:12px;flex:0 0 12px;margin-top:2px}
  .contact a{color:var(--ink)}

  /* learn more */
  .learn{left:910px;top:580px;height:580px;background:var(--cream-light)}
  .learn .copy{padding:22px 18px}
  .learn p{font-size:10px;line-height:16px;color:var(--muted);margin-bottom:16px}
  .learn .photo{position:absolute;left:0;right:0;bottom:0;height:300px;background:linear-gradient(180deg,#e5e7ea,#8c9096 60%,#5d6166)}
</style>
</head>
<body>

<header class="brand">
  <div class="brand-name">SnackHarbor</div>
  <div class="brand-sub">LLC</div>
</header>
<h2 class="deck-label">Landing Page<br>Mobile view</h2>

<section class="screen benefits">
  <div class="top">
    <p class="spec-line">AC110V–120V/220V–240V/50/60Hz</p>
    <span class="btn">More Specifications <svg viewBox="0 0 12 12"><path d="M2 6h8M7 3l3 3-3 3" stroke="#fff" stroke-width="1.5" fill="none"/></svg></span>
  </div>
  <div class="panel">
    <h3>Discover the Benefits of Our Vending Solutions</h3>
    <div class="arrows">
      <span class="arrow-dot off"><svg viewBox="0 0 12 12"><path d="M10 6H2M5 3L2 6l3 3" stroke="#fff" stroke-width="1.5" fill="none"/></svg></span>
      <span class="arrow-dot on"><svg viewBox="0 0 12 12"><path d="M2 6h8M7 3l3 3-3 3" stroke="#fff" stroke-width="1.5" fill="none"/></svg></span>
    </div>
    <div class="cards">
      <article class="benefit-card"><div class="num">1.</div><h4>24/7 Accessibility</h4><p>Enjoy round-the-clock access to refreshments and snacks whenever you need them. Our vending machines are always at your service, catering to your cravings day or night.</p></article>
      <article class="benefit-card"><div class="num">2.</div><h4>Seamless Service</h4><p>Enjoy easy access to snacks and drinks with machines kept stocked for you.</p></article>
    </div>
  </div>
</section>

<section class="screen product product-a">
  <p class="eyebrow">Machine</p>
  <h3>KRX-PDL-47M(B2) Snack And Drink Vending Machine</h3>
  <div class="photo" role="img" aria-label="Snack and drink vending machine against a dark red backdrop" style="height:120px;width:110px;margin:0 auto;background:linear-gradient(135deg,#6a1a1a,#2a2a2a)"></div>
  <div class="thumbs"><span class="active"></span><span></span><span></span><span></span><span></span></div>
  <dl class="spec"><dt>Quantity</dt><dd>60 slots</dd></dl>
</section>

<section class="screen testimonials">
  <article class="review">
    <div class="avatar" role="img" aria-label="Portrait of customer Marisa"></div>
    <h5>Marisa</h5><div class="age">22 Years</div>
    <p>Lorem ipsum dolor sit amet, consectetur adipiscing elit. Nunc vulputate libero et velit interdum, ac aliquet odio mattis.</p>
  </article>
  <article class="review">
    <div class="avatar" role="img" aria-label="Portrait of customer Daniel"></div>
    <h5>Daniel</h5><div class="age">24 Years</div>
    <p>Lorem ipsum dolor sit amet, consectetur adipiscing elit.</p>
  </article>
</section>

<section class="screen inventory">
  <h3>Live Inventory<br>Monitoring</h3>
  <div class="photo" role="img" aria-label="Chilled soda can on a black background" style="height:140px;background:radial-gradient(circle at 45% 55%,#b52a2a 0,#5a1010 22%,#000 45%)"></div>
</section>

<section class="screen hero">
  <div class="bgimg" role="img" aria-label="Close view of a stocked vending machine full of snacks and drinks"></div>
  <div class="shade"></div>
  <div class="hero-bar"><span class="hero-logo">SnackHarbor</span><span class="burger"></span></div>
  <div class="hero-body">
    <h1>Convenience at Your Fingertips: Elevate Your Breaks with Our Vending Solutions</h1>
    <p class="lede">An award-winning SEO agency with disciplines in digital marketing, design, and website development, focused on understanding you.</p>
    <span class="btn">Inquire Now <svg viewBox="0 0 12 12"><path d="M2 6h8M7 3l3 3-3 3" stroke="#fff" stroke-width="1.5" fill="none"/></svg></span>
  </div>
</section>

<section class="screen product product-b">
  <p class="eyebrow">Machine</p>
  <h3>KRX-PDL-47M(B2) Snack And Drink Vending Machine</h3>
  <div class="photo" role="img" aria-label="Snack and drink vending machine against a dark red backdrop" style="height:220px;width:170px;margin:0 auto;background:linear-gradient(135deg,#6a1a1a,#2a2a2a)"></div>
  <div class="thumbs"><span class="active"></span><span></span><span></span><span></span><span></span></div>
  <dl class="spec">
    <dt>Quantity</dt><dd>60 slots</dd>
    <dt>Type</dt><dd>Spiral/conveyor /Pusher</dd>
    <dt>Capacity</dt><dd>All beverages 300 pcs</dd>
    <dt>Weight</dt><dd>261KGS</dd>
  </dl>
</section>

<section class="screen faq-screen">
  <div class="panel">
    <article class="benefit-card"><div class="num">1.</div><h4>24/7 Accessibility</h4><p>Enjoy round-the-clock access to refreshments and snacks whenever you need them. Our vending machines are always at your service, catering to your cravings day or night.</p></article>
    <article class="benefit-card"><div class="num">2.</div><h4>Seamless Service</h4><p>Enjoy easy access to snacks and drinks.</p></article>
  </div>
  <div class="faq-body">
    <p class="eyebrow">FAQ</p>
    <h3>Got Questions? We've Got Answers</h3>
    <div class="faq-item">
      <h5>How can I get more information about your services? <span>⌃</span></h5>
      <p>For further details about our company or products, please contact us by phone or email. If possible, we would like to schedule an in-person meeting at your facility to show you how our services can benefit your team.</p>
    </div>
    <div class="faq-item"><h5>How often do you service the vending machines? <span>⌄</span></h5></div>
  </div>
</section>

<section class="screen footer">
  <div class="footer-logo">SnackHarbor</div>
  <div class="socials"><span></span><span class="light"></span><span></span></div>
  <h6>Page</h6>
  <ul><li>About</li><li>Our Machines</li><li>Services</li><li>Product</li><li>Contact Us</li></ul>
  <h6>Contact</h6>
  <ul class="contact">
    <li><svg viewBox="0 0 12 12"><path d="M3 1l2 2-1 2c1 1.5 2 2.5 3 3l2-1 2 2-2 2C5 11 1 7 1 3z" fill="none" stroke="#333"/></svg><a>(555) 014-2290</a></li>
    <li><svg viewBox="0 0 12 12"><rect x="1" y="2.5" width="10" height="7" fill="none" stroke="#333"/><path d="M1 3l5 4 5-4" fill="none" stroke="#333"/></svg><a>info@snackharbor.com</a></li>
    <li><svg viewBox="0 0 12 12"><circle cx="6" cy="6" r="5" fill="none" stroke="#333"/><path d="M6 3v3l2 1" fill="none" stroke="#333"/></svg>Monday – Saturday 10:00 – 21:00 pm</li>
    <li><svg viewBox="0 0 12 12"><path d="M6 11S2 7 2 4.5a4 4 0 018 0C10 7 6 11 6 11z" fill="none" stroke="#333"/><circle cx="6" cy="4.5" r="1.3" fill="#333"/></svg>48 Harbor Crest Rd #210, Millbrook, Idaho</li>
  </ul>
</section>

<section class="screen learn">
  <div class="copy">
    <p>Lorem ipsum dolor sit amet, consectetur adipiscing elit. Etiam eu tellus. Sed accumsan, nunc tellus elit sed risus velit, sit amet feugiat sociosqu ad litora torquent per inceptos himenaeos.</p>
    <span class="btn">Learn More</span>
  </div>
  <div class="photo" role="img" aria-label="Row of stainless steel snack and drink vending machines in a bright hallway"></div>
</section>

</body>
</html>
```